BOLD & MINIMALIST DESIGN NEEDED

We want a very bold but minimalistic business card design that is impactful and utilizes both sides of the business card. Our current logo is included for your use.

We want bold fonts and good use of negative space. We don't want the logo to overpower the design.

Target Market(s)

Professionals who are building new commercial buildings.

Industry/Entity Type

Construction

Contact Information for Business Card

Name, Title, email, office phone, cell phone, website

Font styles to use
Serif
Sans Serif

Requirements
Must have
• Bold design!

```html
<!DOCTYPE html>
<html lang="en">
<head>
<meta charset="utf-8">
<title>Ridgemont Design + Build — Business Card</title>
<link href="https://fonts.googleapis.com/css2?family=Montserrat:wght@300;400;700;800&display=swap" rel="stylesheet">
<style>
  :root {
    --backdrop: #dcdcdc;
    --paper: #ffffff;
    --ink: #0d0e10;
    --accent: #8fcb55;
    --muted: #7a7a7a;
  }
  * { box-sizing: border-box; margin: 0; padding: 0; }
  html, body { width: 1200px; height: 1200px; overflow: hidden; }
  body {
    background: var(--backdrop);
    font-family: "Montserrat", Arial, sans-serif;
    position: relative;
  }
  .card {
    position: absolute;
    left: 179px;
    width: 861px;
    height: 496px;
    background: var(--paper);
    overflow: hidden;
  }
  .card--front { top: 84px; }
  .card--back { top: 622px; }

  .front-brand {
    position: absolute;
    left: 0; right: 0;
    top: 168px;
    text-align: center;
    color: var(--ink);
    font-weight: 800;
    line-height: 1;
  }
  .front-brand .brand-name { font-size: 62px; letter-spacing: 1px; display: block; }
  .front-brand .brand-tag { font-size: 22px; letter-spacing: 9px; display: block; margin-top: 14px; }

  .back-shapes { position: absolute; inset: 0; width: 100%; height: 100%; }

  .back-brand {
    position: absolute;
    left: 34px;
    top: 48px;
    color: var(--paper);
    font-weight: 800;
    line-height: 1;
    width: 300px;
    text-align: center;
  }
  .back-brand .brand-name { font-size: 49px; letter-spacing: 0.5px; display: block; }
  .back-brand .brand-tag { font-size: 17px; letter-spacing: 7px; display: block; margin-top: 8px; }

  .person {
    position: absolute;
    left: 33px;
    top: 180px;
  }
  .person-name { color: var(--paper); font-weight: 800; font-size: 30px; letter-spacing: 0.5px; }
  .person-title { color: var(--accent); font-weight: 400; font-size: 28px; letter-spacing: 1px; margin-top: 4px; }

  .contact {
    position: absolute;
    display: flex;
    align-items: center;
    gap: 10px;
    color: var(--muted);
    font-weight: 400;
    font-size: 28px;
    letter-spacing: 1.5px;
    line-height: 1;
  }
  .contact svg { width: 28px; height: 28px; flex: none; }
  .contact--mobile { left: 202px; top: 389px; }
  .contact--office { left: 202px; top: 431px; }
  .contact--email { right: 36px; top: 389px; }
  .contact--web { right: 36px; top: 431px; }
  .contact .hl { color: var(--accent); }
</style>
</head>
<body>

  <section class="card card--front" aria-label="Card front">
    <div class="front-brand">
      <span class="brand-name">RIDGEMONT</span>
      <span class="brand-tag">DESIGN + BUILD</span>
    </div>
  </section>

  <section class="card card--back" aria-label="Card back">
    <svg class="back-shapes" viewBox="0 0 1387 797" preserveAspectRatio="none" aria-hidden="true">
      <polygon fill="var(--ink)" points="0,0 1387,0 1387,279 1090,119 0,717"/>
      <polygon fill="var(--accent)" points="1090,131 1387,286 1387,297 1090,170 95,672"/>
    </svg>

    <div class="back-brand">
      <span class="brand-name">RIDGEMONT</span>
      <span class="brand-tag">DESIGN + BUILD</span>
    </div>

    <div class="person">
      <p class="person-name">Name Surename</p>
      <p class="person-title">Director</p>
    </div>

    <div class="contact contact--mobile">
      <svg viewBox="0 0 24 24" aria-hidden="true"><path fill="var(--ink)" d="M6.6 10.8c1.4 2.8 3.8 5.1 6.6 6.6l2.2-2.2c.3-.3.7-.4 1-.2 1.1.4 2.3.6 3.6.6.6 0 1 .4 1 1V20c0 .6-.4 1-1 1C10.6 21 3 13.4 3 4c0-.6.4-1 1-1h3.5c.6 0 1 .4 1 1 0 1.3.2 2.5.6 3.6.1.3 0 .7-.2 1z"/><path fill="none" stroke="var(--ink)" stroke-width="1.6" d="M14 3.5a7 7 0 0 1 6.5 6.5M14 7a3.5 3.5 0 0 1 3 3"/></svg>
      <span>555-014-2200</span>
    </div>
    <div class="contact contact--office">
      <svg viewBox="0 0 24 24" aria-hidden="true"><path fill="var(--ink)" d="M2 8c0-2 4.5-3.5 10-3.5S22 6 22 8v2h-5V8.5c-1.5-.4-3.2-.6-5-.6s-3.5.2-5 .6V10H2zM6 11h12l3 5v5H3v-5zm6 2.5a2.5 2.5 0 1 0 0 5 2.5 2.5 0 0 0 0-5z"/></svg>
      <span>555-014-2200</span>
    </div>
    <div class="contact contact--email">
      <span>info@r-d-b.com</span>
      <svg viewBox="0 0 24 24" aria-hidden="true"><rect x="2" y="5" width="20" height="14" fill="var(--ink)"/><path fill="none" stroke="var(--paper)" stroke-width="1.3" d="M2.5 5.5 12 13l9.5-7.5M2.5 18.5l7-6.5M21.5 18.5l-7-6.5"/></svg>
    </div>
    <div class="contact contact--web">
      <span>www.<span class="hl">r-d-b</span>.com</span>
      <svg viewBox="0 0 24 24" aria-hidden="true"><g fill="none" stroke="var(--ink)" stroke-width="1.5"><circle cx="12" cy="12" r="10"/><ellipse cx="12" cy="12" rx="4.5" ry="10"/><path d="M2 12h20M12 2v20M4 7h16M4 17h16"/></g></svg>
    </div>
  </section>

</body>
</html>
```